Marnick Building Materials letterhead template

Simple but professional letterhead template for business communication.
LOGO/name in upper left, balanced by company contact info on right upper.
Subject description, date...
addressee, cc: and BC: if applicable editable info..

Need extra days to review

```html
<!DOCTYPE html>
<html lang="en">
<head>
<meta charset="utf-8">
<title>Marnick Building Materials – Letterhead</title>
<link rel="stylesheet" href="https://fonts.googleapis.com/css2?family=Open+Sans:wght@400;600&family=DM+Sans:wght@500&display=swap">
<style>
  :root {
    --brand-blue: #2860b0;
    --text-grey: #666a70;
    --text-dark: #333538;
    --page-bg: #ebecef;
    --sheet: #ffffff;
    --sig-fill: #e4e5e8;
  }
  * { margin: 0; padding: 0; box-sizing: border-box; }
  html, body { width: 922px; height: 1200px; overflow: hidden; }
  body {
    background: var(--page-bg);
    font-family: "Open Sans", Arial, sans-serif;
    color: var(--text-grey);
    position: relative;
  }
  .sheet {
    position: absolute;
    left: 33px; top: 0;
    width: 856px; height: 1200px;
    background: var(--sheet);
  }
  .abs { position: absolute; white-space: nowrap; }

  /* brand band */
  .brand-band {
    position: absolute; left: 0; top: 63px;
    width: 295px; height: 100px;
    background: var(--brand-blue);
    border-radius: 0 20px 20px 0;
    display: flex; align-items: center;
    padding-left: 26px;
  }
  .brand-name {
    color: var(--sheet);
    font-weight: 600; font-size: 18px; line-height: 24px;
    white-space: nowrap;
  }

  /* header contacts */
  .header-contacts { position: absolute; left: 590px; top: 0; }
  .contact-row { position: absolute; left: 0; display: flex; align-items: flex-start; gap: 5px; }
  .contact-row svg { flex: none; width: 17px; height: 17px; }
  .contact-row span { font-size: 13px; line-height: 16px; white-space: nowrap; }

  /* sender block */
  .sender-name { left: 75px; top: 315px; font-size: 23.5px; line-height: 32px; color: var(--brand-blue); font-weight: 400; }
  .sender-role { left: 75px; top: 346px; font-size: 12.5px; line-height: 18px; color: var(--text-dark); }
  .details {
    position: absolute; left: 75px; top: 379px;
    display: grid; grid-template-columns: 29px auto;
    font-size: 15px; line-height: 24.3px; white-space: nowrap;
  }
  .details dt { color: var(--brand-blue); font-weight: 600; }
  .details dd { color: var(--text-grey); }

  .letter-date { right: 78px; top: 449px; font-size: 19px; line-height: 24px; }

  .letter-body {
    position: absolute; left: 77px; top: 515px; width: 702px;
    font-size: 14.8px; line-height: 22.4px; text-align: justify;
    word-spacing: -0.3px;
  }
  .letter-body p + p { margin-top: 22.4px; }

  .signature-area { position: absolute; left: 96px; top: 880px; width: 148px; height: 94px; background: var(--sig-fill); border-radius: 4px; }
  .signatory { left: 76px; top: 979px; font-family: "DM Sans", Arial, sans-serif; font-weight: 500; font-size: 26.5px; line-height: 34px; color: var(--text-dark); }
</style>
</head>
<body>
<main class="sheet">
  <header>
    <div class="brand-band">
      <div class="brand-name">Marnick Building Materials</div>
    </div>

    <div class="header-contacts">
      <div class="contact-row" style="top:61px">
        <svg viewBox="0 0 17 17"><rect width="17" height="17" rx="3" fill="var(--brand-blue)"/><path d="M8.5 3.3a3.6 3.6 0 0 0-3.6 3.6c0 2.7 3.6 6.8 3.6 6.8s3.6-4.1 3.6-6.8a3.6 3.6 0 0 0-3.6-3.6zm0 5.1a1.5 1.5 0 1 1 0-3 1.5 1.5 0 0 1 0 3z" fill="#fff"/></svg>
        <span>1820 Harbor Avenue<br>Springfield, IL 62704</span>
      </div>
      <div class="contact-row" style="top:109px">
        <svg viewBox="0 0 17 17"><rect width="17" height="17" rx="3" fill="var(--brand-blue)"/><path d="M5.3 3.6l1.9-.3 1.1 2.6-1.3 1a7 7 0 0 0 3.1 3.1l1-1.3 2.6 1.1-.3 1.9c-.2.6-.7.9-1.3.9A8.9 8.9 0 0 1 4.4 4.9c0-.6.3-1.1.9-1.3z" fill="#fff"/></svg>
        <span>+00 987 654 32</span>
      </div>
      <div class="contact-row" style="top:134px">
        <svg viewBox="0 0 17 17"><rect width="17" height="17" rx="3" fill="var(--brand-blue)"/><rect x="3.5" y="5" width="10" height="7.2" fill="none" stroke="#fff" stroke-width="1.2"/><path d="M3.8 5.4l4.7 3.9 4.7-3.9M3.8 11.8l3.5-3M13.2 11.8l-3.5-3" fill="none" stroke="#fff" stroke-width="1.1"/></svg>
        <span>hello@marnickbm.com</span>
      </div>
      <div class="contact-row" style="top:161px">
        <svg viewBox="0 0 17 17"><rect width="17" height="17" rx="3" fill="var(--brand-blue)"/><path d="M5.5 3.5v9.3l2.3-2.2 1.6 3.3 1.4-.7-1.6-3.2h3.2z" fill="#fff"/></svg>
        <span>www.marnickbm.com</span>
      </div>
    </div>
  </header>

  <section class="sender">
    <h1 class="abs sender-name">Daniel Hart</h1>
    <p class="abs sender-role">Chief Director</p>
    <dl class="details">
      <dt>A :</dt><dd>1820 Harbor Avenue, Springfield, IL 62704</dd>
      <dt>W :</dt><dd>www.marnickbm.com</dd>
      <dt>P :</dt><dd>+00 987 654 32</dd>
      <dt>M :</dt><dd>hello@marnickbm.com</dd>
    </dl>
    <p class="abs letter-date">12 December, 2025</p>
  </section>

  <article class="letter-body">
    <p>Lorem ipsum dolor sit amet, consectetuer adipiscing elit, sed diam nonummy nibh euismod tincidunt ut laoreet dolore magna aliquam erat volutpat. Ut wisi enim ad minim veniam, quis nostrud exerci tation ullamcorper suscipit lobortis nisl ut aliquip ex ea commodo consequat. Duis autem vel eum iriure dolor in hendrerit in vulputate velit esse molestie consequat, vel illum dolore eu feugiat nulla facilisis at vero eros et accumsan et iusto odio dignissim qui blandit praesent luptatum zzril delenit augue duis dolore te feugait nulla facilisi.</p>
    <p>Lorem ipsum dolor sit amet, cons ectetuer adipiscing elit, sed diam nonummy nibh euismod tincidunt ut laoreet dolore magna aliquam erat volutpat. Ut wisi enim ad minim veniam, quis nostrud exerci tation ullamcorper suscipit lobortis nisl ut aliquip ex ea commodo consequat.</p>
    <p>Lorem ipsum dolor sit amet, consectetuer adipiscing elit, sed diam nonummy nibh euismod tincidunt ut laoreet dolore magna aliquam eratveniam, quis nostrud exerci tation ullamcorper suscipit lobortis nisl ut aliquip ex ea commodo consequat. Lorem ipsum dolor sit zamet, consectetuer adipiscing elit, sed diam nonummy nibh euismod tincidunt.</p>
  </article>

  <footer>
    <div class="signature-area" role="img" aria-label="Handwritten signature of the signatory"></div>
    <p class="abs signatory">Mr. Peter Lowell</p>
  </footer>
</main>
</body>
</html>
```